full stationary design for a modern sleek design company

we are a design company that does modern minimalistic interior design works as well as other design services for high end clients.
we need a full stationary design including and not limited to (double sided business card, letter head, envelopes, documents folder...etc) that reflects the modern style design we do.
sleek modern and minimalistic is the requirements.
Updates

please use the latest attached files as there was a slight modification on the logo Added Wednesday, March 1, 2017

minor update on the logo files in JPG and PSD has been updated kindly follow the new attachments. Added Thursday, March 2, 2017

Target Market(s)

modern minimalist clients

Industry/Entity Type

Design Agency

Requirements
Must have
• the logo
Nice to have
• i like the colors in the colored 3D logo attached
Should not have
• too many colors

```html
<!DOCTYPE html>
<html lang="en">
<head>
<meta charset="utf-8">
<title>Linea Atelier — Letterhead</title>
<link href="https://fonts.googleapis.com/css2?family=Montserrat:wght@400;600;700&family=Roboto:wght@400&display=swap" rel="stylesheet">
<style>
  :root {
    --backdrop: #efe3cf;
    --paper: #ffffff;
    --ink: #2b2b2b;
    --accent: #f0891e;
    --accent-deep: #d9692a;
    --band-grey: #b9b9bd;
    --tint: #fbf2e8;
    --muted: #6a6a6a;
  }
  * { margin: 0; padding: 0; box-sizing: border-box; }
  html, body {
    width: 1200px; height: 784px; overflow: hidden;
    background: var(--backdrop);
  }
  .letterhead {
    position: absolute;
    left: 338px; top: 22px;
    width: 523px; height: 740px;
    background:
      radial-gradient(ellipse 120% 90% at 100% 30%, var(--paper) 60%, #fbf9f6 100%);
    box-shadow: 0 6px 18px rgba(120, 90, 50, 0.18);
    overflow: hidden;
  }
  .brand {
    position: absolute; left: 36px; top: 38px;
    display: flex; align-items: flex-start; gap: 8px;
  }
  .brand-square {
    width: 16px; height: 16px; background: var(--accent); margin-top: 2px;
  }
  .brand-name {
    font-family: "Montserrat", sans-serif; font-weight: 700;
    font-size: 17px; letter-spacing: 0.5px; color: var(--ink);
    line-height: 20px;
  }
  .brand-tagline {
    font-family: "Montserrat", sans-serif; font-weight: 600;
    font-size: 7.5px; letter-spacing: 3.6px; color: var(--accent);
    margin-top: 2px;
  }
  .contact-tint {
    position: absolute; right: 0; top: 44px;
    width: 112px; height: 120px; background: var(--tint); opacity: 0.7;
  }
  .contact {
    position: absolute; right: 22px; top: 40px; width: 150px;
    font-family: "Roboto", sans-serif; color: var(--muted);
  }
  .contact-name {
    font-family: "Montserrat", sans-serif; font-weight: 700;
    font-size: 8.5px; color: var(--ink); letter-spacing: 0.4px;
    margin-bottom: 3px;
  }
  .contact-line {
    display: flex; align-items: center; gap: 5px;
    font-size: 6.6px; line-height: 9px;
  }
  .contact-line .dot {
    width: 5px; height: 5px; border-radius: 50%; background: var(--accent);
    flex: none;
  }
  .contact-line.no-dot { padding-left: 10px; }
  .corner-mark {
    position: absolute; right: 40px; bottom: 30px;
    width: 96px; height: 96px; background: var(--tint);
  }
  .footer-band {
    position: absolute; left: 0; bottom: 0; width: 100%; height: 7px;
    display: flex;
  }
  .footer-band .band-accent {
    width: 62%; background: linear-gradient(90deg, var(--accent-deep), var(--accent));
  }
  .footer-band .band-gap { width: 2%; background: var(--paper); }
  .footer-band .band-grey {
    flex: 1; background: linear-gradient(90deg, #9d9da2, var(--band-grey));
  }
</style>
</head>
<body>
  <main class="letterhead">
    <header class="brand">
      <span class="brand-square"></span>
      <div>
        <div class="brand-name">LINEA ATELIER</div>
        <div class="brand-tagline">BY MARC DELORME</div>
      </div>
    </header>

    <div class="contact-tint"></div>
    <address class="contact">
      <div class="contact-name">LINEA ATELIER</div>
      <div class="contact-line"><span class="dot"></span>Sample Road, Suite 200,</div>
      <div class="contact-line no-dot">Austin, TX 78701</div>
      <div class="contact-line"><span class="dot"></span>(000) 555-0142</div>
      <div class="contact-line"><span class="dot"></span>(000) 555-0187</div>
      <div class="contact-line"><span class="dot"></span>hello@lineaatelier.com</div>
      <div class="contact-line no-dot">www.lineaatelier.com</div>
    </address>

    <div class="corner-mark"></div>
    <div class="footer-band">
      <span class="band-accent"></span>
      <span class="band-gap"></span>
      <span class="band-grey"></span>
    </div>
  </main>
</body>
</html>
```